Updated DJ business Card showing other businesses

DJ Kestro offers professional mobile dj services including DJ. MC. Karaoke.
Silent Disco (will attach logo)
I also offer a 360 Photo Booth.

Contact info:
(555) 013-4472
marcus.tellgren@lumomail.net
Social Media @DJKestroNWX

```html
<!DOCTYPE html>
<html lang="en">
<head>
<meta charset="utf-8">
<title>DJ Kestro – Business Card</title>
<link rel="stylesheet" href="https://fonts.googleapis.com/css2?family=Jost:wght@400;600;700&display=swap">
<style>
  :root {
    --backdrop: #d6d6d6;
    --card-pink: #d4214a;
    --ink-black: #111111;
    --paper-white: #ffffff;
    --soft-white: rgba(255,255,255,0.88);
  }
  * { box-sizing: border-box; margin: 0; padding: 0; }
  html, body {
    width: 1200px; height: 913px; overflow: hidden;
    background: var(--backdrop);
    font-family: "Jost", sans-serif;
  }
  .stage {
    width: 1200px; height: 913px;
    display: flex; align-items: center; justify-content: center; gap: 40px;
  }
  .card {
    width: 540px; height: 309px;
    background: var(--card-pink);
    position: relative;
    box-shadow: 0 18px 36px rgba(0,0,0,0.25);
  }
  /* Front: services and contact */
  .card-front { padding: 26px 30px 22px; color: var(--paper-white); }
  .brand-name {
    font-size: 44px; font-weight: 700; line-height: 1; letter-spacing: 0.5px;
  }
  .tagline { font-size: 16px; font-weight: 600; margin-top: 12px; letter-spacing: 0.4px; }
  .services { font-size: 27px; font-weight: 700; margin-top: 2px; letter-spacing: 1px; }
  .photo-booth-band {
    margin-top: 12px;
    background: var(--ink-black);
    border-radius: 22px;
    height: 42px;
    display: flex; align-items: center; justify-content: center;
    font-size: 20px; font-weight: 700; letter-spacing: 0.6px;
  }
  .card-footer {
    position: absolute; left: 30px; right: 30px; bottom: 20px;
    display: flex; justify-content: space-between; align-items: flex-end;
  }
  .side-brand { display: flex; align-items: center; gap: 10px; }
  .side-brand .mark {
    width: 42px; height: 42px; border-radius: 50%; background: var(--ink-black);
  }
  .side-brand .label { font-size: 22px; font-weight: 700; color: var(--paper-white); }
  .contact-list { list-style: none; font-size: 13px; font-weight: 400; color: var(--soft-white); line-height: 1.55; }
  .contact-list li { display: flex; align-items: center; gap: 6px; }
  .contact-list svg { width: 12px; height: 12px; flex: none; }
  .contact-list .no-icon { padding-left: 18px; }
  /* Back: silent disco name */
  .card-back { display: flex; align-items: center; justify-content: center; gap: 18px; }
  .card-back .mark {
    width: 64px; height: 64px; border-radius: 50%; background: var(--ink-black);
  }
  .card-back .label {
    font-size: 40px; font-weight: 700; line-height: 1; color: var(--paper-white);
  }
</style>
</head>
<body>
<main class="stage">
  <section class="card card-front" aria-label="Business card front">
    <h1 class="brand-name">DJ Kestro</h1>
    <p class="tagline">offers professional Mobile Dj Services including</p>
    <p class="services">DJ. MC. Karaoke</p>
    <p class="photo-booth-band">I also offer a 360 Photo Booth.</p>
    <div class="card-footer">
      <div class="side-brand">
        <span class="mark"></span>
        <span class="label">Silent Disco</span>
      </div>
      <ul class="contact-list">
        <li>
          <svg viewBox="0 0 12 12" aria-hidden="true"><path d="M2.5 1h2l1 3-1.3 1a6 6 0 0 0 2.8 2.8l1-1.3 3 1v2c0 .6-.4 1-1 1A10 10 0 0 1 1.5 2c0-.6.4-1 1-1z" fill="#111"/></svg>
          (555) 013-4472
        </li>
        <li>
          <svg viewBox="0 0 12 12" aria-hidden="true"><rect x="0.5" y="2" width="11" height="8" fill="#111"/><path d="M0.5 2 6 6.5 11.5 2" stroke="#d4214a" stroke-width="1" fill="none"/></svg>
          marcus.tellgren@lumomail.net
        </li>
        <li class="no-icon">Social Media @DJKestroNWX</li>
      </ul>
    </div>
  </section>

  <section class="card card-back" aria-label="Business card back">
    <span class="mark"></span>
    <span class="label">Silent Disco</span>
  </section>
</main>
</body>
</html>
```